QDN Advisory needs business card

Having just developed a logo, I now want to use that logo in the development of a business card. The card should contain the logo, my name, title, phone, email, website and physical address. I would like to use one side of the card for details and the other side for logo and messaging. Use your creativity to place the information effectively. I want the logo to appear in a strong blue, which may be matched on the back side of the card, where the logo might be reversed out in white. I want the text to be in either dark blue or black (not light blue or gray).
I am consultant, primarily helping small and mid-size companies refine their strategy, reorganize their staff and propel forward in their industry. I also teach at universities and coach on a one-on-one basis. The final design should reflect expertise, guidance, judgement, perspective, experience.
The font used in the logo is ACaslonPro.

Target Market(s)

small to mid-size companies in the US seeking business guidance

Industry/Entity Type

Business

Font styles to use
Other font styles liked:
• ACaslonPro

Colors
0455a3
0255a3
3277b5

Requirements
Must have
• Card must convey my name and information clearly. Do not make it too small - many of my customers are 50+ years old. Please use all three of my titles: consultant / coach / instructor.
Should not have
• Please do not use icons to represent the phone, email, web. Do not use p / e / w either to indicate those details.

I have decided that a swatch of color, especially a "blue wave," does not work for me. I would rather have a simpler, more reserved look rather than a very contemporary, high color card.

Please do not deconstruct the logo or put it in a different font or italics.

```html
<!DOCTYPE html>
<html lang="en">
<head>
<meta charset="utf-8">
<title>QDN Advisory – Business Card</title>
<link rel="stylesheet" href="https://fonts.googleapis.com/css2?family=Libre+Caslon+Text:wght@400;700&family=Open+Sans:wght@400;600&display=swap">
<style>
  :root {
    --brand-blue: #0455a3;
    --brand-blue-mid: #3277b5;
    --card-blue: #2a86e2;
    --card-blue-light: #4aa0ee;
    --ink: #0255a3;
    --paper: #ffffff;
    --backdrop: #ddd8d1;
    --rule-light: #bcdcf7;
  }
  * { box-sizing: border-box; margin: 0; padding: 0; }
  html, body {
    width: 1200px;
    height: 442px;
    overflow: hidden;
    background: var(--backdrop);
  }
  .stage {
    position: relative;
    width: 1200px;
    height: 442px;
    display: flex;
    align-items: center;
    justify-content: center;
    gap: 50px;
  }
  .card {
    position: relative;
    width: 540px;
    height: 310px;
    box-shadow: 0 6px 18px rgba(0,0,0,0.25);
  }

  /* Front: details side */
  .card--front {
    background: var(--paper);
    font-family: "Libre Caslon Text", Georgia, serif;
    color: var(--ink);
  }
  .brand {
    position: absolute;
    left: 36px;
    top: 84px;
    display: flex;
    align-items: center;
    gap: 10px;
  }
  .brand__square {
    width: 22px;
    height: 22px;
    background: var(--brand-blue);
  }
  .brand__name {
    font-family: "Libre Caslon Text", Georgia, serif;
    font-weight: 400;
    font-size: 28px;
    line-height: 1.2;
    color: var(--brand-blue);
    letter-spacing: 0.3px;
    white-space: nowrap;
  }
  .contact {
    position: absolute;
    right: 30px;
    top: 26px;
    text-align: right;
    font-size: 14.5px;
    line-height: 1.45;
  }
  .contact__address { margin-top: 10px; }
  .person {
    position: absolute;
    right: 30px;
    bottom: 36px;
    text-align: right;
  }
  .person__name {
    font-weight: 700;
    font-size: 16px;
    line-height: 20px;
  }
  .person__name small { font-size: 13px; font-weight: 400; }
  .person__title {
    font-size: 14px;
    line-height: 20px;
    margin-top: 14px;
  }
  .person-rule {
    position: absolute;
    right: 30px;
    bottom: 62px;
    width: 460px;
    height: 2px;
    background: linear-gradient(to right, rgba(255,255,255,0), var(--rule-light) 40%, var(--brand-blue-mid));
  }

  /* Back: logo side */
  .card--back {
    background: radial-gradient(ellipse at 48% 45%, var(--card-blue-light) 0%, var(--card-blue) 70%);
    color: var(--paper);
    display: flex;
    flex-direction: column;
    align-items: center;
    justify-content: center;
    gap: 26px;
  }
  .brand--reversed {
    position: static;
    gap: 16px;
  }
  .brand--reversed .brand__square {
    width: 38px;
    height: 38px;
    background: var(--paper);
  }
  .brand--reversed .brand__name {
    color: var(--paper);
    font-size: 52px;
  }
  .web {
    font-family: "Open Sans", Arial, sans-serif;
    font-size: 15px;
    letter-spacing: 1.5px;
  }
</style>
</head>
<body>
<main class="stage">
  <section class="card card--front" aria-label="Business card front">
    <div class="brand">
      <span class="brand__square"></span>
      <span class="brand__name">QDN Advisory</span>
    </div>
    <div class="contact">
      <p>407-555-0148</p>
      <p>warren@qdn-advisory.com</p>
      <p>www.qdn-advisory.com</p>
      <p class="contact__address">7412 Brenwick Court<br>Orlando, FL 32806</p>
    </div>
    <div class="person-rule"></div>
    <div class="person">
      <p class="person__name">J. Warren Hollister,<small>CCIM</small></p>
      <p class="person__title">Consultant, Coach &amp; Instructor</p>
    </div>
  </section>

  <section class="card card--back" aria-label="Business card back">
    <div class="brand brand--reversed">
      <span class="brand__square"></span>
      <span class="brand__name">QDN Advisory</span>
    </div>
    <p class="web">www.qdn-advisory.com</p>
  </section>
</main>
</body>
</html>
```